Guitar parts retail packaging

I have 2 boxes I need designed. This will be for my guitar parts. They are going to be thick cardstock type paper box, with a foam insert to secure the items. Matte finish with silver foil printing is sort of where im headed, but Im open to other beautiful design. The boxes will need to have a window on top of the box to show the product inside. Color scheme Im thinking with is Black with red, white and Silver foil printing. Unless you come up with something nicer, im open to that. But my business cards and some stickers are those colors.
2 different size boxes, but they can be the same basic design, modified for 2 different sizes. They will open at the front, and the lid will lift, hinged at the top back edge. (Please see purple box in picture for example for how box will work). Both boxes will have a window on top to showcase product in the box. One of the sides, (2" X 1.25") will be left a solid color, grey or other so I can put a product sticker on that side to designate what type of product is in the box. So you are really just designing the top (With window), front, back, and 1 side. Maybe something clever on the bottom but if thats blank thats fine.
LARGE BOX:
5.25 wide (Left to right)
2” deep (Front to back)
1.25” tall (Top to bottom)
SMALL BOX:
2” Wide (Left to right)
2” Deep (Front to back)
Please see Business card and sticker in picture for color scheme Im thinking. ( I am open to other colors and designs as well)

Target Market(s)

Musicians, Rockers, tattoo junkies, general badasses.

Industry/Entity Type

Guitar industry. Rock & Rollers

Font styles to use
Other font styles liked:
• I use a font called Morpheus for my logo. Also Times New Roman, maybe Copperplate? Or something more creative? Im open as long as it fits.

Colors
EB3D1F
EC4F4E
F09395
F8D3D4
FCEDEE

Requirements
Must have
• My Company name and logo (Harrow Kestrel). Also slogan-
Nice to have
• Please see general aesthetic in sticker and biz card.
Should not have
• No horror themes, keep it cool and classy. (Even though logo is a skull). And please no pictures of guitars on the box. You might add a pic of 1 type of guitar, but the parts inside might not fit that guitar pictured on the box.

```html
<!DOCTYPE html>
<html lang="en">
<head>
<meta charset="utf-8">
<title>Harrow Kestrel – Box Dielines</title>
<link rel="stylesheet" href="https://fonts.googleapis.com/css2?family=Cinzel:wght@500&family=Montserrat:wght@700&display=swap">
<style>
  :root {
    --paper: #ffffff;
    --box-red-light: #8a2219;
    --box-red-dark: #4e0f0c;
    --die-edge: #3a0907;
    --fold-line: #2f8fd6;
    --window-dark: #2a1010;
    --window-clear: #ffffff;
    --foil-gold: #c9a15a;
    --ink-white: #f4ecec;
  }
  html, body {
    margin: 0;
    width: 1200px;
    height: 900px;
    overflow: hidden;
    background: var(--paper);
  }
  .dieline-sheet {
    position: absolute;
    left: 0;
    top: 225px;
    width: 1200px;
    height: 451px;
  }
  .brand-name {
    font-family: "Cinzel", serif;
    font-weight: 500;
    fill: var(--foil-gold);
    text-anchor: middle;
  }
  .brand-url {
    font-family: "Montserrat", sans-serif;
    font-weight: 700;
    fill: var(--ink-white);
    text-anchor: middle;
    letter-spacing: 0.5px;
  }
  .brand-mark-name {
    font-family: "Cinzel", serif;
    font-weight: 500;
    fill: var(--foil-gold);
    text-anchor: middle;
  }
  .die-body { stroke: var(--die-edge); stroke-width: 4; }
  .fold { stroke: var(--fold-line); stroke-width: 1.2; stroke-dasharray: 6 5; fill: none; }
  .window-top { fill: var(--window-dark); }
  .window-front { fill: var(--window-clear); stroke: var(--fold-line); stroke-width: 1.5; }
</style>
</head>
<body>
<svg class="dieline-sheet" viewBox="110 200 1650 620" xmlns="http://www.w3.org/2000/svg">
  <defs>
    <linearGradient id="boxStock" x1="0" y1="0" x2="1" y2="1">
      <stop offset="0" stop-color="var(--box-red-dark)"/>
      <stop offset="0.5" stop-color="var(--box-red-light)"/>
      <stop offset="1" stop-color="var(--box-red-dark)"/>
    </linearGradient>
  </defs>

  <!-- Large box dieline -->
  <g class="dieline dieline-large">
    <path class="die-body" role="img" aria-label="Deep red damask swirl pattern across the box stock" fill="url(#boxStock)"
      d="M315,230 L412,225 L790,225 L888,230 L888,315 L1068,315 L1068,475 L888,475 L888,555 L860,565 Q888,565 888,590 L888,670 Q888,690 860,697 Q888,705 888,728 Q888,752 860,762 L790,800 L412,800 L345,770 Q315,755 315,730 Q315,705 343,697 Q315,690 315,670 L315,590 Q315,565 343,565 L315,555 L315,475 L133,475 L133,315 L315,315 Z"/>
    <line class="fold" x1="412" y1="225" x2="412" y2="800"/>
    <line class="fold" x1="790" y1="225" x2="790" y2="800"/>
    <line class="fold" x1="322" y1="320" x2="880" y2="320"/>
    <line class="fold" x1="322" y1="470" x2="880" y2="470"/>
    <line class="fold" x1="322" y1="555" x2="880" y2="555"/>
    <line class="fold" x1="322" y1="700" x2="880" y2="700"/>
    <line class="fold" x1="232" y1="320" x2="232" y2="470"/>
    <line class="fold" x1="322" y1="235" x2="322" y2="548"/>
    <line class="fold" x1="880" y1="235" x2="880" y2="548"/>
    <line class="fold" x1="970" y1="320" x2="970" y2="470"/>
    <rect class="fold" x="142" y="322" width="916" height="146"/>

    <rect class="window-top" x="420" y="333" width="360" height="125"/>
    <rect class="window-front" x="483" y="600" width="235" height="57"/>

    <text class="brand-mark-name" x="600" y="278" font-size="15">Harrow</text>
    <text class="brand-mark-name" x="600" y="296" font-size="15">Kestrel</text>
    <g transform="translate(367,395) rotate(90)">
      <text class="brand-mark-name" y="-2" font-size="14">Harrow</text>
      <text class="brand-mark-name" y="14" font-size="14">Kestrel</text>
    </g>
    <g transform="translate(833,395) rotate(-90)">
      <text class="brand-mark-name" y="-2" font-size="14">Harrow</text>
      <text class="brand-mark-name" y="14" font-size="14">Kestrel</text>
    </g>
    <text class="brand-mark-name" x="443" y="626" font-size="13">Harrow</text>
    <text class="brand-mark-name" x="443" y="642" font-size="13">Kestrel</text>
    <text class="brand-mark-name" x="759" y="626" font-size="13">Harrow</text>
    <text class="brand-mark-name" x="759" y="642" font-size="13">Kestrel</text>

    <g transform="rotate(180 600 505)">
      <text class="brand-name" x="600" y="502" font-size="36">Harrow Kestrel</text>
      <text class="brand-url" x="600" y="526" font-size="11">HARROWKESTREL.COM</text>
    </g>
    <text class="brand-name" x="600" y="755" font-size="38">Harrow Kestrel</text>
    <text class="brand-url" x="600" y="775" font-size="12">HARROWKESTREL.COM</text>
  </g>

  <!-- Small box dieline -->
  <g class="dieline dieline-small">
    <path class="die-body" role="img" aria-label="Deep red damask swirl pattern across the box stock" fill="url(#boxStock)"
      d="M1228,230 L1327,225 L1470,225 L1568,230 L1568,315 L1713,315 L1713,475 L1568,475 L1568,555 L1540,565 Q1568,565 1568,590 L1568,670 Q1568,690 1540,697 Q1568,705 1568,728 Q1568,752 1540,762 L1470,800 L1327,800 L1258,770 Q1228,755 1228,730 Q1228,705 1256,697 Q1228,690 1228,670 L1228,590 Q1228,565 1256,565 L1228,555 L1228,475 L1085,475 L1085,315 L1228,315 Z"/>
    <line class="fold" x1="1327" y1="225" x2="1327" y2="800"/>
    <line class="fold" x1="1470" y1="225" x2="1470" y2="800"/>
    <line class="fold" x1="1236" y1="320" x2="1560" y2="320"/>
    <line class="fold" x1="1236" y1="470" x2="1560" y2="470"/>
    <line class="fold" x1="1236" y1="555" x2="1560" y2="555"/>
    <line class="fold" x1="1236" y1="700" x2="1560" y2="700"/>
    <line class="fold" x1="1146" y1="320" x2="1146" y2="470"/>
    <line class="fold" x1="1236" y1="235" x2="1236" y2="548"/>
    <line class="fold" x1="1560" y1="235" x2="1560" y2="548"/>
    <line class="fold" x1="1650" y1="320" x2="1650" y2="470"/>
    <rect class="fold" x="1093" y="322" width="612" height="146"/>

    <rect class="window-top" x="1336" y="333" width="126" height="125"/>
    <rect class="window-front" x="1370" y="600" width="56" height="57"/>

    <text class="brand-mark-name" x="1398" y="278" font-size="14">Harrow</text>
    <text class="brand-mark-name" x="1398" y="295" font-size="14">Kestrel</text>
    <g transform="translate(1285,395) rotate(90)">
      <text class="brand-mark-name" y="-2" font-size="13">Harrow</text>
      <text class="brand-mark-name" y="13" font-size="13">Kestrel</text>
    </g>
    <g transform="translate(1512,395) rotate(-90)">
      <text class="brand-mark-name" y="-2" font-size="13">Harrow</text>
      <text class="brand-mark-name" y="13" font-size="13">Kestrel</text>
    </g>
    <text class="brand-mark-name" x="1346" y="627" font-size="8">Harrow</text>
    <text class="brand-mark-name" x="1346" y="637" font-size="8">Kestrel</text>
    <text class="brand-mark-name" x="1452" y="627" font-size="8">Harrow</text>
    <text class="brand-mark-name" x="1452" y="637" font-size="8">Kestrel</text>

    <g transform="rotate(180 1398 508)">
      <text class="brand-name" x="1398" y="505" font-size="17">Harrow Kestrel</text>
      <text class="brand-url" x="1398" y="517" font-size="6">HARROWKESTREL.COM</text>
    </g>
    <text class="brand-name" x="1398" y="750" font-size="19">Harrow Kestrel</text>
    <text class="brand-url" x="1398" y="761" font-size="6">HARROWKESTREL.COM</text>
  </g>
</svg>
</body>
</html>
```